Need Business Cards for my Business

email address: klmvertexcalibration@mailcove.com
web address: klmvertexcalibration.com
Slogan: We offer various NRB licenses
Wallace R. Pendry
Please stick with colors of Company Logo
would like the card to be more of the color example of the logo.
If you need PDF copy of logo email me at the above account.
Creative control rests with you.

Industry/Entity Type

Business

Contact Information for Business Card

I am a minimalist, but would like something to pop and stand out amongst other cards, make it memorable.

Font styles to use
Serif
Decorative
Script

```html
<!DOCTYPE html>
<html lang="en">
<head>
<meta charset="utf-8">
<title>Vertex Calibration – Business Cards</title>
<link href="https://fonts.googleapis.com/css2?family=Open+Sans:wght@400;600;700&display=swap" rel="stylesheet">
<style>
  :root {
    --page-bg: #e9ebee;
    --navy: #1f3f73;
    --blue: #2a62a8;
    --blue-light: #3a7cc4;
    --name-blue: #2e6bb5;
    --red: #d9262c;
    --white: #ffffff;
    --ink: #1d1d1f;
  }
  * { box-sizing: border-box; margin: 0; padding: 0; }
  html, body { width: 1200px; height: 901px; overflow: hidden; }
  body {
    background: var(--page-bg);
    font-family: "Open Sans", Arial, sans-serif;
    position: relative;
  }
  .card {
    position: absolute;
    width: 525px;
    height: 300px;
    border-radius: 3px;
    overflow: hidden;
    box-shadow: 0 6px 18px rgba(0,0,0,0.18);
  }
  /* Front card */
  .card-front {
    left: 50px;
    top: 300px;
    background: radial-gradient(ellipse at 40% 35%, var(--blue-light) 0%, var(--blue) 45%, var(--navy) 100%);
    color: var(--white);
  }
  .card-front .brand {
    position: absolute;
    left: 0; right: 0; top: 100px;
    display: flex; justify-content: center; align-items: center; gap: 12px;
  }
  .brand-mark {
    width: 16px; height: 16px;
    background: var(--red);
    flex: none;
  }
  .card-front .brand-name {
    font-size: 30px; font-weight: 700; letter-spacing: 0.5px; color: var(--white);
  }
  .card-front .slogan {
    position: absolute;
    left: 0; right: 0; top: 200px;
    text-align: center;
    font-size: 17px;
    letter-spacing: 0.4px;
  }
  /* Back card */
  .card-back {
    left: 625px;
    top: 300px;
    background: var(--white);
  }
  .card-back .brand {
    position: absolute;
    left: 40px; top: 40px;
    display: flex; align-items: center; gap: 10px;
  }
  .card-back .brand-name {
    font-size: 24px; font-weight: 700; color: var(--navy);
  }
  .contact {
    position: absolute;
    left: 40px; top: 150px;
    font-size: 13px; color: var(--ink);
    list-style: none;
  }
  .contact li { display: flex; align-items: center; gap: 8px; margin-bottom: 6px; }
  .contact svg { width: 12px; height: 12px; fill: var(--navy); flex: none; }
  .person {
    position: absolute;
    right: 40px; top: 160px;
    text-align: left;
  }
  .person-name { font-size: 19px; color: var(--name-blue); font-weight: 400; }
  .person-title { font-size: 13px; color: var(--ink); }
  .footer-band {
    position: absolute; left: 0; bottom: 0; width: 525px; height: 70px;
  }
  .web {
    position: absolute;
    right: 36px; bottom: 10px;
    font-size: 14px; color: var(--white); letter-spacing: 0.3px;
  }
</style>
</head>
<body>
  <section class="card card-front">
    <div class="brand">
      <span class="brand-mark"></span>
      <span class="brand-name">Vertex Calibration</span>
    </div>
    <p class="slogan">We offer various NRB licenses</p>
  </section>

  <section class="card card-back">
    <div class="brand">
      <span class="brand-mark"></span>
      <span class="brand-name">Vertex Calibration</span>
    </div>

    <ul class="contact">
      <li>
        <svg viewBox="0 0 12 12"><path d="M2.5 0.5 L4.5 0.5 L5 3.2 L3.6 4.3 Q4.6 6.8 7.7 8.4 L8.8 7 L11.5 7.5 L11.5 9.5 Q11.5 11.5 9.5 11.5 Q0.5 10 0.5 2.5 Q0.5 0.5 2.5 0.5 Z"/></svg>
        410-555-0184
      </li>
      <li>
        <svg viewBox="0 0 12 12"><path d="M0 2 L12 2 L12 10 L0 10 Z M0.8 2.6 L6 6.6 L11.2 2.6" stroke="#fff" stroke-width="0.8"/></svg>
        klmvertexcalibration@mailcove.com
      </li>
    </ul>

    <div class="person">
      <p class="person-name">Wallace R. Pendry</p>
      <p class="person-title">Manager</p>
    </div>

    <svg class="footer-band" viewBox="0 0 525 70" preserveAspectRatio="none">
      <path d="M0 14 L250 66 L260 40 L525 40 L525 70 L0 70 Z" fill="var(--navy)"/>
      <path d="M0 6 L258 58 L256 63 L0 11 Z" fill="var(--red)"/>
      <path d="M0 11 L256 63 L252 66 L0 15 Z" fill="var(--white)"/>
    </svg>
    <p class="web">www.klmvertexcalibration.com</p>
  </section>
</body>
</html>
```